Website for a health information tech company

I need a website for a new startup company, Lumivale, Inc. that specializes in healthcare information technology. Lumivale is a monitoring system that uses wearable sensors and predictive algorithms to detect when an elderly persons health is declining and triggers progressively higher levels of interventions.

The site needs to be very simple, elegant and initially will have minimal information as company and product is still under development and is in a stealth mode. I like the tandovix.com website as it has a "single page" look and feel with sliding vertical sections. Ideally the sections would be "Home", "Technology", "Customers", "News", "About Us" and "Contact Us". The contact us should have a contact form that gets sent to an email address.

I have a couple of example sites that my site should take inspiration from (tandovix.com and brimholtway.com). I would like a WordPress backend so I can easily update content so the winning design should be easily importable or setup into Wordpress.

Target Market(s)

Investors, Customers (Doctors, Patients, Health Insurance companies, Hospital directors)

Industry/Entity Type

Healthcare

Requirements
Must have
• top horizontal menu that gets repeated on each vertical slide. Should have animated vertical slides. Must be viewable on any device (iPad, Android Tablets) correctly and must render correctly on different screen sizes. Must be viewable in all popular browsers. Must work well with touchscreen devices such as iPad, iPhone, Android tablets and phones.
Must have a content management system backend such as WordPress so I can edit/update content and in future add additional sections, images etc.

See attached company logo so colors must be complimentary to the logo colors. Feel free to use the logo colors as web site theme colors if it makes sense.
Nice to have
• Nice subtle textured background like linen or leather.
Should not have
• Not looking for traditional web site design with nav bars on left etc
Should not feel like a traditional web site where you click a link and another page loads. It must be animated slide into a different section. No flash or any other technology that requires plug ins.

```html
<!DOCTYPE html>
<html lang="en">
<head>
<meta charset="utf-8">
<title>Lumivale — Home</title>
<link rel="stylesheet" href="https://fonts.googleapis.com/css2?family=Source+Sans+3:wght@400;600&display=swap">
<style>
  :root {
    --orange: #f57f20;
    --orange-dark: #e06a0c;
    --ink: #3a3a3a;
    --text: #555555;
    --muted: #8a8a8a;
    --line: #d8d8d8;
    --dark-band: #3b3b3b;
    --footer: #6b6b6b;
    --white: #ffffff;
    --icon: #7a7a7a;
  }
  * { box-sizing: border-box; margin: 0; padding: 0; }
  html, body { width: 1200px; height: 1010px; overflow: hidden; background: var(--white); }
  body { position: relative; font-family: "Source Sans 3", "Myriad Pro", Arial, sans-serif; color: var(--text); }
  .abs { position: absolute; }

  /* header */
  .site-header { position: absolute; left: 0; top: 0; width: 1200px; height: 83px; background: var(--white); border-bottom: 1px solid #cfcfcf; z-index: 2; }
  .brand { left: 182px; top: 20px; display: flex; align-items: center; gap: 8px; font-size: 20px; font-weight: 600; color: var(--orange); }
  .brand-mark { width: 14px; height: 14px; background: var(--orange); border-radius: 50%; }
  .main-nav a { position: absolute; top: 31px; height: 26px; line-height: 26px; font-size: 11.5px; color: var(--ink); text-decoration: none; text-transform: uppercase; }
  .main-nav a.active { background: var(--orange); color: var(--white); border-radius: 2px; width: 70px; text-align: center; border: 1px solid var(--orange-dark); }

  /* hero */
  .hero { left: 0; top: 83px; width: 1200px; height: 389px; background: linear-gradient(90deg, #d4d7dc 0%, #eeeff1 30%, #e2e4e8 60%, #cfd2d7 100%); }
  .hero-tag { left: 180px; top: 195px; width: 186px; height: 35px; background: var(--orange); color: var(--white); font-size: 18px; line-height: 35px; padding-left: 17px; }
  .hero-title { left: 180px; top: 238px; width: 375px; height: 35px; background: var(--dark-band); color: var(--white); font-size: 13.5px; font-weight: 600; line-height: 35px; padding-left: 17px; }
  .hero-copy { left: 183px; top: 285px; width: 340px; font-size: 9.5px; line-height: 17px; color: var(--ink); }
  .btn-start { left: 186px; top: 355px; width: 164px; height: 37px; background: linear-gradient(#5a5a5a, #3a3a3a); color: #eee; border: 1px solid #777; border-radius: 3px; font-size: 14px; line-height: 35px; text-align: center; }
  .slide-arrow { top: 258px; width: 29px; height: 29px; background: rgba(255,255,255,0.45); border-radius: 3px; }
  .slide-arrow svg { display: block; margin: 7px auto; }
  .devices { left: 604px; top: 161px; width: 400px; height: 336px; border-radius: 12px; background: linear-gradient(160deg, #2c2c2c 0%, #5a5a5a 55%, #cfcfcf 100%); }

  /* welcome */
  .laptop { left: 190px; top: 543px; width: 384px; height: 226px; border-radius: 10px 10px 4px 4px; background: linear-gradient(120deg, #2a2a2a, #6c7075 60%, #3a3d40); }
  .welcome-title { left: 622px; top: 574px; font-size: 21px; color: var(--ink); font-weight: 400; }
  .welcome-copy { left: 623px; top: 611px; width: 330px; font-size: 9.5px; line-height: 17px; color: var(--text); }

  /* contact widget */
  .touch { left: 1010px; top: 524px; width: 190px; height: 72px; border: 1px solid var(--line); border-right: none; background: var(--white); }
  .touch-title { position: absolute; left: 52px; top: 12px; font-size: 12.5px; font-weight: 600; color: var(--orange); letter-spacing: 0.3px; }
  .touch-close { position: absolute; right: 6px; top: 6px; width: 10px; height: 10px; border: 1px solid #aaa; border-radius: 50%; }
  .touch-input { position: absolute; left: 12px; top: 39px; width: 121px; height: 18px; border: 1px solid var(--line); font-size: 7.5px; line-height: 16px; padding-left: 6px; color: var(--muted); }
  .touch-submit { position: absolute; left: 133px; top: 39px; width: 47px; height: 18px; background: var(--orange); color: var(--white); font-size: 7.5px; line-height: 18px; text-align: center; }

  /* roles */
  .divider-band { left: 3px; top: 801px; width: 1197px; height: 8px; background: linear-gradient(#e2e2e2, #fafafa); }
  .role { top: 840px; }
  .role h3 { position: absolute; font-size: 14px; font-weight: 400; color: var(--orange); white-space: nowrap; }
  .role p { position: absolute; top: 24px; font-size: 9.5px; line-height: 15px; color: var(--muted); width: 130px; }
  .role-sep { top: 848px; width: 1px; height: 52px; background: var(--line); }

  /* footer */
  .site-footer { left: 1px; top: 938px; width: 1199px; height: 72px; background: var(--footer); }
  .footer-nav { left: 186px; top: 958px; display: flex; font-size: 8px; color: var(--white); }
  .footer-nav span { padding: 0 18px; border-left: 1px solid #ddd; line-height: 9px; }
  .footer-nav span:first-child { padding-left: 0; border-left: none; }
  .copyright { left: 186px; top: 980px; font-size: 8px; color: var(--white); }
  .social { top: 965px; width: 12px; height: 12px; border-radius: 50%; background: #cfcfcf; }
</style>
</head>
<body>

<header class="site-header">
  <div class="abs brand"><span class="brand-mark"></span>Lumivale</div>
  <nav class="main-nav">
    <a class="active" href="#home" style="left:460px">Home</a>
    <a href="#technology" style="left:567px">Technology</a>
    <a href="#customers" style="left:696px">Customers</a>
    <a href="#about" style="left:818px">About Us</a>
    <a href="#contact" style="left:930px">Contact Us</a>
  </nav>
</header>

<section class="abs hero" role="img" aria-label="Softly blurred office background photograph"></section>
<div class="abs slide-arrow" style="left:114px"><svg width="10" height="14"><path d="M8 1 L2 7 L8 13" stroke="#bbb" fill="none" stroke-width="1.5"/></svg></div>
<div class="abs slide-arrow" style="left:1039px"><svg width="10" height="14"><path d="M2 1 L8 7 L2 13" stroke="#bbb" fill="none" stroke-width="1.5"/></svg></div>
<div class="abs hero-tag">LUMIVALE IS A</div>
<h1 class="abs hero-title">LUMIVALE IS A PATENT PENDING MONITORING SYSTEM</h1>
<p class="abs hero-copy">Lumivale is a patent pending monitoring system that uses wearable sensors and predictive algorithms to detect when an elderly persons health is declining and triggers progressively higher levels of interventions.</p>
<div class="abs btn-start">GET STARTED NOW</div>
<div class="abs devices" role="img" aria-label="Desktop monitor, tablet and phone showing the website"></div>

<div class="abs laptop" role="img" aria-label="Laptop playing a video of a hand touching a screen beside server racks"></div>
<h2 class="abs welcome-title">WELCOME TO LUMIVALE</h2>
<p class="abs welcome-copy">Lumivale is a patent pending monitoring system that uses wearable sensors and predictive algorithms to detect when an elderly persons health is declining and triggers progressively higher levels of interventions.<br>The goal is to allow an elderly person, who often has 2 or more chronic conditions, to age in place and stay independent as long as possible by the use of intelligent monitoring to deliver just in time care.</p>

<aside class="abs touch">
  <svg class="abs" style="left:18px;top:8px" width="30" height="24" viewBox="0 0 30 24"><path d="M1 12 L29 1 L22 23 L15 15 Z" fill="var(--orange)"/><path d="M15 15 L29 1" stroke="#fff" stroke-width="1"/></svg>
  <div class="touch-title">GET IN TOUCH</div>
  <span class="touch-close"></span>
  <div class="touch-input">ENTER YOUR EMAIL ID</div>
  <div class="touch-submit">SUBMIT</div>
</aside>

<div class="abs divider-band"></div>

<svg class="abs" style="left:181px;top:840px" width="86" height="60" viewBox="0 0 86 60" fill="none" stroke="var(--icon)" stroke-width="3">
  <rect x="18" y="2" width="64" height="46" rx="3"/><rect x="2" y="14" width="36" height="44" rx="3" fill="#fff"/><rect x="66" y="26" width="18" height="32" rx="3" fill="#fff"/>
</svg>
<div class="abs role" style="left:281px"><h3>CASE MANAGER</h3><p>Lumivale is a patent pending monitoring system.</p></div>
<div class="abs role-sep" style="left:419px"></div>
<svg class="abs" style="left:435px;top:845px" width="62" height="56" viewBox="0 0 62 56" fill="none" stroke="var(--icon)" stroke-width="3">
  <rect x="2" y="2" width="58" height="42" rx="3"/><path d="M26 44 L24 54 L38 54 L36 44" fill="var(--icon)"/>
</svg>
<div class="abs role" style="left:513px"><h3>HEALTH AIDE</h3><p>Lumivale is a patent pending monitoring system.</p></div>
<div class="abs role-sep" style="left:653px"></div>
<svg class="abs" style="left:669px;top:846px" width="43" height="53" viewBox="0 0 43 53" fill="none" stroke="var(--icon)" stroke-width="3">
  <rect x="2" y="2" width="39" height="49" rx="3"/><rect x="8" y="8" width="27" height="37"/>
</svg>
<div class="abs role" style="left:725px"><h3>ADMIN</h3><p>Lumivale is a patent pending monitoring system.</p></div>
<div class="abs role-sep" style="left:851px"></div>
<svg class="abs" style="left:870px;top:849px" width="26" height="46" viewBox="0 0 26 46" fill="none" stroke="var(--icon)" stroke-width="3">
  <rect x="2" y="2" width="22" height="42" rx="4"/><rect x="6" y="9" width="14" height="26"/><circle cx="13" cy="39" r="1.5" fill="var(--icon)"/>
</svg>
<div class="abs role" style="left:908px"><h3>CLINICIAN</h3><p>Lumivale is a patent pending monitoring system.</p></div>

<footer class="abs site-footer"></footer>
<nav class="abs footer-nav"><span>HOME</span><span>TECHNOLOGY</span><span>CUSTOMERS</span><span>ABOUT US</span><span>CONTACT US</span></nav>
<div class="abs copyright">© COPYRIGHTS 2013 LUMIVALE. ALL RIGHTS RESERVED</div>
<span class="abs social" style="left:833px"></span>
<span class="abs social" style="left:867px"></span>
<span class="abs social" style="left:902px"></span>
<span class="abs social" style="left:935px"></span>
<span class="abs social" style="left:966px"></span>
<span class="abs social" style="left:999px"></span>

</body>
</html>
```